Criação de Papelaria (6 itens) para Beleza
A empresa queria:
" DISTRIBUO PRODUTOS PROFISSIONAIS DE COSMÉTICOS PARA PROFISSIONAIS "CABELEIREIROS". A MARCA QUE DISTRIBUIMOS CHAMA-SE "VALIRO" http://www.valiroprofissional.com.br/ "

```html
<!DOCTYPE html>
<html lang="pt-BR">
<head>
<meta charset="UTF-8">
<title>Lumera Cosméticos — Papel Timbrado</title>
<link href="https://fonts.googleapis.com/css2?family=Montserrat:wght@400;600;700&display=swap" rel="stylesheet">
<style>
  :root {
    --backdrop: #e9e9e9;
    --paper: #ffffff;
    --teal: #1f6b73;
    --gold: #c9a13b;
    --ink-soft: #8a9a9c;
    --mark-faint: #eef0f0;
  }
  * { margin: 0; padding: 0; box-sizing: border-box; }
  html, body {
    width: 1200px; height: 1200px; overflow: hidden;
    background: var(--backdrop);
    font-family: "Montserrat", sans-serif;
  }
  .letterhead {
    position: absolute; left: 220px; top: 63px;
    width: 760px; height: 1074px;
    background: var(--paper);
    box-shadow: 0 6px 24px rgba(0,0,0,0.12);
  }
  .brand { position: absolute; display: flex; align-items: center; gap: 14px; }
  .brand--header { left: 56px; top: 58px; }
  .brand--footer { left: 40px; bottom: 30px; gap: 8px; }
  .brand-dot { border-radius: 50%; background: var(--gold); }
  .brand--header .brand-dot { width: 40px; height: 40px; }
  .brand--footer .brand-dot { width: 18px; height: 18px; }
  .brand-text { display: flex; flex-direction: column; color: var(--teal); font-weight: 700; line-height: 1; }
  .brand--header .brand-name { font-size: 52px; }
  .brand--header .brand-tag { font-size: 11px; font-weight: 400; letter-spacing: 4px; margin-top: 4px; padding-left: 60px; }
  .brand--footer .brand-name { font-size: 26px; }
  .brand--footer .brand-tag { font-size: 6px; font-weight: 400; letter-spacing: 2px; margin-top: 2px; padding-left: 30px; }
  .faint-mark {
    position: absolute; left: 240px; top: 360px;
    width: 270px; height: 270px; border-radius: 50%;
    background: var(--mark-faint);
  }
  .contact-band {
    position: absolute; right: 0; bottom: 40px;
    width: 470px; height: 62px;
    background: var(--teal); color: #fff;
    display: flex; justify-content: space-between; align-items: center;
    padding: 0 22px 0 20px;
    font-size: 9px;
  }
  .contact-list { list-style: none; display: flex; flex-direction: column; gap: 4px; }
  .contact-list li { display: flex; align-items: center; gap: 6px; }
  .contact-list svg { width: 9px; height: 9px; fill: #fff; }
  .contact-city { letter-spacing: 1px; font-weight: 600; }
</style>
</head>
<body>
  <main class="letterhead">
    <header class="brand brand--header">
      <span class="brand-dot"></span>
      <div class="brand-text">
        <span class="brand-name">Lumera</span>
        <span class="brand-tag">COSMÉTICOS</span>
      </div>
    </header>

    <div class="faint-mark"></div>

    <footer>
      <div class="brand brand--footer">
        <span class="brand-dot"></span>
        <div class="brand-text">
          <span class="brand-name">Lumera</span>
          <span class="brand-tag">COSMÉTICOS</span>
        </div>
      </div>
      <div class="contact-band">
        <ul class="contact-list">
          <li><svg viewBox="0 0 10 10"><path d="M2 0.5 L4 2.5 L3 4 Q4.5 6 6 7 L7.5 6 L9.5 8 L8 9.5 Q3 9 0.5 2 Z"/></svg>(63) 3000-0000</li>
          <li><svg viewBox="0 0 10 10"><path d="M0 2 H10 V8 H0 Z M0 2 L5 6 L10 2" /></svg>contato@lumeracosmeticos.com.br</li>
          <li><svg viewBox="0 0 10 10"><circle cx="5" cy="5" r="4.5"/></svg>www.lumeracosmeticos.com.br</li>
        </ul>
        <span class="contact-city">PALMAS • TO • BRASIL</span>
      </div>
    </footer>
  </main>
</body>
</html>
```